Flyer Design

Create a flyer using the logo theme. Single page for to be sent out on email. Attached is an image of the layout, below is the text. A5 and a4 versions.

Simplifying the MAZE

This short workshop is designed as a refresher for those surgeons who have attended a full Lund-MAZE training course, and wish to gain an update on the latest thinking with regards to the surgical treatment of Atrial Fibrillation.
We will start with an overview of the disease burden, talk to the foundation clinical evidence available, and cover the various lesion sets used by surgeons – with a view to simplifying the procedure. The workshop will also explain the technology used, how to treat the Left Atrial Appendage, the best ways to work with your EP colleagues, and involve a short hands-on session to familiarize you with the tools available to perform the Lund-MAZE procedure.

Faculty
{{image}}
Mr. Declan Harlow
Cardiothoracic Surgeon

Mr Harlows training was completed at the Brenhill Clinic, Rochester, Minnesota, between June 1995 and July 1997 followed by an advanced fellowship with Professor Ferris K Lomond at the Ashgrove General Hospital. Additional expertise required visits to Belgium, Italy, England and the United States. Mr Harlow now proctors internationally in order to share his knowledge and further improvement in all areas of minimal access and open cardiac and thoracic surgery.
Further overseas experience at the Ashgrove General Hospital in Canada culminated in the award of Clinical Fellowship in Cardiovascular Surgery in December 1997.

Mr Harlow has contributed to many publications and is referee for Journal articles in very highly regarded professional journals. He performs both Cardiac surgery procedures and thoracic procedures at Westmere Private Hospital and Dunmore Hospital, Melbourne. Mr Harlow has performed in excess of 200 open Maze procedures and 35 via a Thoracoscopic approach.

Venue - TBA
Time : 5pm - 7.30pm, followed by dinner and case presentations

```html
<!DOCTYPE html>
<html lang="en">
<head>
<meta charset="utf-8">
<title>Simplifying the MAZE – Workshop Flyer</title>
<link href="https://fonts.googleapis.com/css2?family=Roboto:ital,wght@0,300;0,400;0,700;1,300&family=Source+Sans+3:wght@400&display=swap" rel="stylesheet">
<style>
  :root {
    --brand-blue: #2071ac;
    --deep-blue: #18476e;
    --accent-orange: #f9800f;
    --title-blue: #2a93e2;
    --venue-blue: #2a6fa8;
    --ink: #111111;
    --paper: #ffffff;
    --photo-tone: #b9b3ab;
  }
  * { margin: 0; padding: 0; box-sizing: border-box; }
  html, body { width: 860px; height: 1200px; overflow: hidden; background: var(--paper); }
  .flyer { position: relative; width: 860px; height: 1200px; overflow: hidden; background: var(--paper); font-family: "Source Sans 3", "Myriad Pro", sans-serif; color: var(--ink); }
  .waves { position: absolute; inset: 0; }
  .brand { position: absolute; left: 47px; top: 52px; width: 215px; height: 90px; border-radius: 50%; background: var(--paper); display: flex; align-items: center; justify-content: center; }
  .brand-name { font-family: "Roboto", sans-serif; font-weight: 400; font-size: 40px; color: var(--brand-blue); letter-spacing: -0.5px; }
  .headline { position: absolute; font-family: "Roboto", sans-serif; font-weight: 700; color: var(--title-blue); font-size: 38px; line-height: 1; }
  .headline.title { left: 377px; top: 61px; }
  .headline.faculty { left: 440px; top: 400px; }
  .copy { position: absolute; right: 55px; text-align: right; font-size: 15.2px; line-height: 19.6px; }
  .intro-1 { top: 128px; }
  .intro-2 { top: 237px; right: 57px; }
  .bio-1 { top: 727px; right: 62px; }
  .bio-2 { top: 887px; right: 64px; }
  .portrait-ring { position: absolute; left: 403px; top: 451px; width: 200px; height: 200px; border-radius: 50%; border: 1.5px solid var(--accent-orange); }
  .portrait { position: absolute; left: 411px; top: 459px; width: 184px; height: 184px; border-radius: 50%; background: radial-gradient(circle at 50% 40%, #d8cfc6 0%, var(--photo-tone) 55%, #3a3f44 100%); }
  .speaker-name { position: absolute; left: 0; width: 1004px; text-align: center; top: 655px; font-family: "Roboto", sans-serif; font-weight: 700; font-size: 24px; }
  .speaker-role { position: absolute; left: 0; width: 1004px; text-align: center; top: 684px; font-family: "Roboto", sans-serif; font-weight: 300; font-style: italic; font-size: 19px; }
  .venue { position: absolute; left: 546px; top: 1030px; display: flex; align-items: center; gap: 8px; font-family: "Roboto", sans-serif; font-size: 36px; color: var(--venue-blue); }
  .time { position: absolute; right: 78px; top: 1080px; text-align: right; font-family: "Roboto", sans-serif; font-size: 26px; line-height: 30px; color: var(--accent-orange); }
</style>
</head>
<body>
<main class="flyer">
  <svg class="waves" width="860" height="1200" viewBox="0 0 860 1200" aria-hidden="true">
    <rect width="860" height="1200" fill="var(--brand-blue)"/>
    <path d="M270,0 C290,120 270,250 200,400 C120,570 52,680 50,800 C48,960 130,1090 232,1200 L860,1200 L860,0 Z" fill="var(--deep-blue)"/>
    <path d="M302,0 C312,120 282,260 222,390 C142,560 94,680 94,800 C94,960 160,1085 245,1200 L860,1200 L860,0 Z" fill="var(--accent-orange)"/>
    <path d="M322,0 C332,130 300,260 240,390 C160,560 115,680 115,800 C115,960 200,1090 317,1200 L860,1200 L860,0 Z" fill="var(--paper)"/>
  </svg>

  <div class="brand"><span class="brand-name">Cardiora</span></div>

  <h1 class="headline title">Simplifying the MAZE</h1>

  <p class="copy intro-1">This short workshop is designed as a refresher for those surgeons<br>who have attended a full Lund-MAZE training course, and wish to<br>gain an update on the latest thinking with regards to the surgical<br>treatment of Atrial Fibrillation.</p>

  <p class="copy intro-2">We will start with an overview of the disease burden, talk to the foundation<br>clinical evidence available, and cover the various lesion sets used by surgeons –<br>with a view to simplifying the procedure. The workshop will also explain the<br>technology used, how to treat the Left Atrial Appendage, the best ways to work<br>with your EP colleagues, and involve a short hands-on session to familiarize you<br>with the tools available to perform the Lund-MAZE procedure.</p>

  <h2 class="headline faculty">Faculty</h2>

  <div class="portrait-ring"></div>
  <div class="portrait" role="img" aria-label="Portrait photo of the faculty surgeon"></div>

  <p class="speaker-name">Mr. Declan Harlow</p>
  <p class="speaker-role">Cardiothoracic Surgeon</p>

  <p class="copy bio-1">Mr Harlows training was completed at the Brenhill Clinic, Rochester, Minnesota, between June 1995<br>and July 1997 followed by an advanced fellowship with Professor Ferris K Lomond at the Ashgrove<br>General Hospital. Additional expertise required visits to Belgium, Italy, England and the United<br>States. Mr Harlow now proctors internationally in order to share his knowledge and further impro-<br>vement in all areas of minimal access and open cardiac and thoracic surgery.<br>Further overseas experience at the Ashgrove General Hospital in Canada culminated in the award<br>of Clinical Fellowship in Cardiovascular Surgery in December 1997.</p>

  <p class="copy bio-2">Mr Harlow has contributed to many publications and is referee for Journal articles in very<br>highly regarded professional journals. He performs both Cardiac surgery procedures<br>and thoracic procedures at Westmere Private Hospital and Dunmore Hospital, Melbourne.<br>Mr Harlow has performed in excess of 200 open Maze procedures and 35 via a<br>Thoracoscopic approach.</p>

  <div class="venue">
    <svg width="22" height="32" viewBox="0 0 22 32" aria-hidden="true">
      <path d="M11,1.5 C5.5,1.5 1.5,5.8 1.5,11 C1.5,18 11,30 11,30 C11,30 20.5,18 20.5,11 C20.5,5.8 16.5,1.5 11,1.5 Z" fill="none" stroke="var(--title-blue)" stroke-width="2"/>
      <circle cx="11" cy="11" r="3.8" fill="none" stroke="var(--title-blue)" stroke-width="2"/>
    </svg>
    <span>Venue - TBA</span>
  </div>

  <p class="time">Time : 5pm - 7.30pm,<br>followed by dinner and case presentations</p>
</main>
</body>
</html>
```